Quiz A Legal Tutor

We need banner ad design for a new company that supplies supplemental study materials for law students. All content on the site is completely free and we assist law students with supplemental materials for daily course work and for preparing for final exams. The site provides free: Q&A - all answers provided by law professors, Audio Lectures on the most important law school topics, Outline Overviews, Charts and Notes of difficult and confusing law school topics, mini essays with answers for exam preparation.
Updates

ads need to be in the following sizes: 728x90, 160x600, 300x250, 468x60, 120x240

Reason: the ad target market are 'professional students' so it cannot look childish in design. The design must be professional looking.

Target Market(s)

Law Students .. review the QuizALegalTutor.com site

Industry/Entity Type

School

Requirements
Must have
• The word 'Free' must be very prominent throughout the ads
Nice to have
• Try to include 'all of the free items' that are included that the user receives once the register for free for the site. Also the ads may include animation so that each free item the user receives may be able to stand out better.

```html
<!DOCTYPE html>
<html lang="en">
<head>
<meta charset="utf-8">
<title>Quiz A Legal Tutor – Banner Set</title>
<link href="https://fonts.googleapis.com/css2?family=Roboto+Condensed:wght@400;500;700&display=swap" rel="stylesheet">
<style>
  :root {
    --stage: #1b1b1b;
    --brand-blue: #0b80c6;
    --accent-yellow: #ffd400;
    --button-yellow: #ffcc00;
    --button-shadow: #b58f00;
    --tick-green: #3be33a;
    --text-white: #ffffff;
    --text-dark: #1a1a1a;
    --photo-light: #e4dcd6;
    --photo-mid: #8a7970;
    --photo-dark: #2c2522;
  }
  * { box-sizing: border-box; margin: 0; padding: 0; }
  html, body { width: 1200px; height: 744px; overflow: hidden; }
  body {
    background: var(--stage);
    font-family: "Roboto Condensed", "Arial Narrow", sans-serif;
    color: var(--text-white);
    position: relative;
  }
  .banner {
    position: absolute;
    background: var(--brand-blue);
    overflow: hidden;
    box-shadow: 0 0 0 1px rgba(255,255,255,0.25);
  }
  .photo {
    position: absolute;
    background: linear-gradient(170deg, var(--photo-light) 0%, var(--photo-mid) 50%, var(--photo-dark) 100%);
  }
  .brand-name {
    position: absolute;
    display: flex;
    align-items: center;
    gap: 6px;
    color: var(--text-dark);
    font-weight: 700;
    white-space: nowrap;
    line-height: 1;
  }
  .brand-name .mark {
    width: 10px; height: 10px;
    background: var(--brand-blue);
    flex: none;
  }
  .headline { text-align: center; font-weight: 500; line-height: 1.05; }
  .headline .lead { display: block; }
  .headline .tutor { display: block; color: var(--accent-yellow); font-weight: 700; }
  .rule { position: absolute; height: 1px; background: rgba(255,255,255,0.55); }
  .perks { list-style: none; position: absolute; line-height: 1.03; }
  .perks li { position: relative; padding-left: 13px; }
  .perks li::before { content: "✓"; position: absolute; left: 0; color: var(--tick-green); font-weight: 700; }
  .cta {
    position: absolute;
    background: var(--button-yellow);
    color: var(--text-dark);
    font-weight: 500;
    display: flex;
    align-items: center;
    justify-content: center;
    gap: 6px;
    box-shadow: 0 3px 0 var(--button-shadow);
    white-space: nowrap;
  }
  .cta .arrow { font-weight: 700; }

  /* Skyscraper 160x600 */
  .skyscraper { left: 101px; top: 31px; width: 176px; height: 661px; }
  .skyscraper .photo { left: 0; top: 0; width: 176px; height: 358px; }
  .skyscraper .brand-name { left: 10px; top: 16px; font-size: 17px; }
  .skyscraper .headline { position: absolute; left: 0; top: 372px; width: 176px; }
  .skyscraper .headline .lead { font-size: 19px; }
  .skyscraper .headline .tutor { font-size: 42px; line-height: 1; }
  .skyscraper .headline .sub { display: block; font-size: 17px; line-height: 1.25; letter-spacing: -0.3px; }
  .skyscraper .rule { left: 10px; top: 495px; width: 156px; }
  .skyscraper .perks { left: 15px; top: 505px; font-size: 15px; }
  .skyscraper .cta { left: 18px; top: 614px; width: 140px; height: 35px; font-size: 20px; }

  /* Medium rectangle 300x250 */
  .rectangle { left: 288px; top: 300px; width: 330px; height: 276px; }
  .rectangle .photo { left: 165px; top: 0; width: 165px; height: 276px; }
  .rectangle .brand-name { left: 174px; top: 14px; font-size: 16px; }
  .rectangle .headline { position: absolute; left: 0; top: 6px; width: 165px; }
  .rectangle .headline .lead { font-size: 19px; }
  .rectangle .headline .tutor { font-size: 40px; line-height: 1; }
  .rectangle .headline .sub { display: block; font-size: 17px; line-height: 1.2; letter-spacing: -0.3px; }
  .rectangle .rule { left: 22px; top: 121px; width: 120px; }
  .rectangle .perks { left: 12px; top: 130px; font-size: 14px; }
  .rectangle .cta { left: 14px; top: 232px; width: 133px; height: 33px; font-size: 19px; }

  /* Leaderboard 728x90 */
  .leaderboard { left: 288px; top: 586px; width: 802px; height: 99px; }
  .leaderboard .photo { left: 0; top: 0; width: 305px; height: 99px; }
  .leaderboard .brand-name { left: 150px; top: 12px; font-size: 16px; }
  .leaderboard .headline { position: absolute; left: 305px; top: 16px; width: 212px; }
  .leaderboard .headline .lead { display: inline; font-size: 21px; }
  .leaderboard .headline .tutor { display: inline; font-size: 21px; font-weight: 500; }
  .leaderboard .headline .sub { display: block; font-size: 17px; line-height: 1.3; letter-spacing: -0.3px; }
  .leaderboard .divider { position: absolute; left: 518px; top: 10px; width: 1px; height: 78px; background: rgba(255,255,255,0.55); }
  .leaderboard .perks { left: 525px; top: 4px; font-size: 14px; line-height: 0.98; }
  .leaderboard .cta { left: 664px; top: 37px; width: 127px; height: 33px; font-size: 19px; }
</style>
</head>
<body>

<section class="banner skyscraper" aria-label="Quiz A Legal Tutor skyscraper banner">
  <div class="photo" role="img" aria-label="Photo of a smiling law student holding notebooks in a lecture hall"></div>
  <div class="brand-name"><span class="mark"></span>Quiz A Legal Tutor</div>
  <h2 class="headline">
    <span class="lead">Your Personal</span>
    <span class="tutor">TUTOR</span>
    <span class="sub">&amp; Everything Resource<br>for Legal Education</span>
  </h2>
  <div class="rule"></div>
  <ul class="perks">
    <li>Q &amp; A.</li>
    <li>Topic Videos/Audio<br>lectures.</li>
    <li>Outline Overviews.</li>
    <li>Charts and Notes.</li>
    <li>Mini Essays.</li>
  </ul>
  <a class="cta">TRY IT FREE <span class="arrow">»</span></a>
</section>

<section class="banner rectangle" aria-label="Quiz A Legal Tutor rectangle banner">
  <div class="photo" role="img" aria-label="Photo of a smiling law student holding notebooks in a lecture hall"></div>
  <div class="brand-name"><span class="mark"></span>Quiz A Legal Tutor</div>
  <h2 class="headline">
    <span class="lead">Your Personal</span>
    <span class="tutor">TUTOR</span>
    <span class="sub">&amp; Everything Resource<br>for Legal Education</span>
  </h2>
  <div class="rule"></div>
  <ul class="perks">
    <li>Q &amp; A.</li>
    <li>Topic Videos/Audio<br>lectures.</li>
    <li>Outline Overviews.</li>
    <li>Charts and Notes.</li>
    <li>Mini Essays.</li>
  </ul>
  <a class="cta">TRY IT FREE <span class="arrow">»</span></a>
</section>

<section class="banner leaderboard" aria-label="Quiz A Legal Tutor leaderboard banner">
  <div class="photo" role="img" aria-label="Photo of a smiling law student with classmates in a lecture hall"></div>
  <div class="brand-name"><span class="mark"></span>Quiz A Legal Tutor</div>
  <h2 class="headline">
    <span class="lead">Your Personal </span><span class="tutor">TUTOR</span>
    <span class="sub">&amp; Everything Resource for<br>Legal Education</span>
  </h2>
  <div class="divider"></div>
  <ul class="perks">
    <li>Q &amp; A.</li>
    <li>Topic Videos/Audio<br>lectures.</li>
    <li>Outline Overviews.</li>
    <li>Charts and Notes.</li>
    <li>Mini Essays.</li>
  </ul>
  <a class="cta">TRY IT FREE <span class="arrow">»</span></a>
</section>

</body>
</html>
```